Book Cover for a technology book - The Silent Lattice

We are writing a book that is a handbook how to build a hybrid cloud - this is a technology concept where companies use cloud services both from the like of Vornix or Plenquor and also cloud services built in there own data centers - hence the term hybrid cloud. We want a book cover with the title - The Silent Lattice; which signifies that we will be teaching companies how to build a hybrid cloud that just works. We want the tagline - handbook for building Hybrid Clouds. The authors are Corwin Haddle and Ross Pelley. The cover is to be engaging and feel different than your usual technical manual. I don't have any graphics to help out however will be able to refine and tell you what I don and don't like based on your drafts. The book dimensions are yet to be determined, in the first instance it will be a PDF

Target Market(s)

technology executives and specialists

Industry/Entity Type

Information Technology

Colors

Designer to choose colors to be used in the design.

Requirements
Nice to have
• While I don't have a particular view to how it will look, I'd like the style to be more casual than ultra formal

```html
<!DOCTYPE html>
<html lang="en">
<head>
<meta charset="utf-8">
<title>The Silent Lattice — Book Cover</title>
<link href="https://fonts.googleapis.com/css2?family=Tinos:wght@400;700&display=swap" rel="stylesheet">
<style>
  :root {
    --stage: #1c1a1f;
    --cover-top: #4b3f8e;
    --cover-bottom: #433985;
    --band: #2e2560;
    --ink: #ffffff;
    --art-light: #8fd8f0;
    --art-mid: #5aa9dc;
    --art-deep: #4b3f8e;
  }
  * { margin: 0; padding: 0; box-sizing: border-box; }
  html, body {
    width: 801px;
    height: 1200px;
    overflow: hidden;
    background: var(--stage);
  }
  .canvas {
    position: relative;
    width: 801px;
    height: 1200px;
  }
  .book-cover {
    position: absolute;
    left: 62px;
    top: 85px;
    width: 683px;
    height: 1035px;
    background: linear-gradient(180deg, var(--cover-top) 0%, var(--cover-bottom) 100%);
    font-family: "Tinos", "Times New Roman", serif;
    color: var(--ink);
    overflow: hidden;
  }
  .authors {
    position: absolute;
    top: 22px;
    left: 0;
    width: 100%;
    text-align: center;
    font-size: 40px;
    font-variant: small-caps;
    letter-spacing: 0.5px;
    line-height: 1;
  }
  .cover-art {
    position: absolute;
    left: 60px;
    top: 100px;
    width: 540px;
    height: 470px;
    border-radius: 40px;
    background:
      radial-gradient(ellipse 55% 40% at 55% 38%, var(--art-light) 0%, var(--art-mid) 45%, rgba(90,169,220,0) 75%),
      radial-gradient(ellipse 70% 55% at 50% 60%, rgba(90,169,220,0.35) 0%, rgba(75,63,142,0) 80%);
  }
  .title {
    font-weight: 400;
  }
  .title-line {
    position: absolute;
    left: 0;
    width: 100%;
    text-align: center;
    line-height: 1;
    white-space: nowrap;
  }
  .title-the {
    top: 595px;
    font-size: 60px;
  }
  .title-main {
    top: 639px;
    font-size: 120px;
  }
  .title-last {
    top: 749px;
    font-size: 120px;
  }
  .tagline-band {
    position: absolute;
    left: 0;
    top: 880px;
    width: 100%;
    height: 54px;
    background: var(--band);
    display: flex;
    align-items: center;
    justify-content: center;
    font-size: 34px;
    line-height: 1;
  }
</style>
</head>
<body>
  <div class="canvas">
    <section class="book-cover">
      <p class="authors">Corwin Haddle &amp; Ross Pelley</p>
      <div class="cover-art" role="img" aria-label="Illustration of a glowing blue isometric cloud with a download arrow and circuit lines branching below, over faint hexagons"></div>
      <h1 class="title">
        <span class="title-line title-the">THE</span>
        <span class="title-line title-main">SILENT</span>
        <span class="title-line title-last">LATTICE</span>
      </h1>
      <p class="tagline-band">Handbook for building Hybrid Clouds</p>
    </section>
  </div>
</body>
</html>
```